VORN - Business cards

Business card to be created for Commercial sales staff

Target Market(s)

Commercial businesses

Industry/Entity Type

Commercial

Contact Information for Business Card

Look professional. For commercial clients

Colors
ffffff

Requirements
Must have
• - Vorn Logo
• - Commercial sales staff as postion
• - room for commerical sales manager role
• - person name and their mobile number
• - Website : vornelectrical.com.au
Nice to have
• White background.
• On back of business card just have the logo no other information
Should not have
• Should only have white background on front of card.

```html
<!DOCTYPE html>
<html lang="en">
<head>
<meta charset="utf-8">
<title>VORN – Business Cards</title>
<link rel="stylesheet" href="https://fonts.googleapis.com/css2?family=Roboto:ital,wght@0,400;0,500;0,900;1,400&display=swap">
<style>
  :root {
    --stage: #e6e6e6;
    --card: #ffffff;
    --brand-red: #c8161d;
    --brand-ink: #35363a;
    --text-grey: #5a5b5e;
    --shadow: rgba(0, 0, 0, 0.18);
  }
  * { margin: 0; padding: 0; box-sizing: border-box; }
  html, body {
    width: 1200px;
    height: 900px;
    overflow: hidden;
    background: var(--stage);
    font-family: "Roboto", Arial, sans-serif;
  }
  .stage {
    position: relative;
    width: 1200px;
    height: 900px;
  }
  .card {
    position: absolute;
    left: 300px;
    width: 600px;
    height: 343px;
    background: var(--card);
    box-shadow: 0 10px 28px var(--shadow);
    overflow: hidden;
  }
  .card--front { top: 70px; }
  .card--back { top: 480px; }

  .wordmark {
    position: absolute;
    display: flex;
    align-items: center;
    gap: 14px;
    color: var(--brand-ink);
    font-weight: 900;
    letter-spacing: 2px;
    line-height: 1;
    white-space: nowrap;
  }
  .wordmark__dot {
    border-radius: 50%;
    background: var(--brand-red);
    flex: none;
  }
  .card--front .wordmark {
    left: 50%;
    top: 50%;
    transform: translate(-50%, -50%);
    font-size: 104px;
  }
  .card--front .wordmark__dot { width: 40px; height: 40px; }

  .card--back .wordmark {
    left: 300px;
    top: 128px;
    font-size: 70px;
  }
  .card--back .wordmark__dot { width: 28px; height: 28px; }

  .accent-bar {
    position: absolute;
    left: 0;
    top: 26px;
    width: 7px;
    height: 30px;
    background: var(--brand-red);
  }
  .identity {
    position: absolute;
    left: 30px;
    top: 26px;
  }
  .identity__name {
    color: var(--brand-red);
    font-size: 18px;
    font-weight: 500;
  }
  .identity__role {
    color: var(--text-grey);
    font-size: 13px;
    font-style: italic;
    margin-top: 2px;
  }

  .contact {
    position: absolute;
    left: 30px;
    top: 178px;
    color: var(--text-grey);
    font-size: 14px;
    line-height: 20px;
    list-style: none;
  }
  .contact__address { margin-bottom: 6px; }
  .contact__item {
    display: flex;
    align-items: center;
    gap: 6px;
  }
  .contact__icon {
    width: 12px;
    height: 12px;
    flex: none;
    fill: none;
    stroke: var(--brand-red);
    stroke-width: 1.6;
  }
</style>
</head>
<body>
<main class="stage">

  <section class="card card--front" aria-label="Card front">
    <div class="wordmark">
      <span class="wordmark__dot"></span>
      <span class="wordmark__text">VORN</span>
    </div>
  </section>

  <section class="card card--back" aria-label="Card back">
    <span class="accent-bar"></span>
    <div class="identity">
      <p class="identity__name">Daniel Reyes</p>
      <p class="identity__role">Commercial Sales Manager</p>
    </div>

    <div class="wordmark">
      <span class="wordmark__dot"></span>
      <span class="wordmark__text">VORN</span>
    </div>

    <ul class="contact">
      <li class="contact__address">Street name, Suite 100<br>State, Zip Code, Country</li>
      <li class="contact__item">
        <svg class="contact__icon" viewBox="0 0 12 12"><rect x="3" y="1" width="6" height="10" rx="1"/><line x1="5" y1="9" x2="7" y2="9"/></svg>
        013-579-2468
      </li>
      <li class="contact__item">
        <svg class="contact__icon" viewBox="0 0 12 12"><rect x="1" y="2.5" width="10" height="7"/><polyline points="1,2.5 6,6.5 11,2.5"/></svg>
        info@vornelectrical.com.au
      </li>
      <li class="contact__item">
        <svg class="contact__icon" viewBox="0 0 12 12"><circle cx="6" cy="6" r="5"/><ellipse cx="6" cy="6" rx="2.2" ry="5"/><line x1="1" y1="6" x2="11" y2="6"/></svg>
        vornelectrical.com.au
      </li>
    </ul>
  </section>

</main>
</body>
</html>
```